Financial Services Business Card Design

We are a financial services company Based in London, offering Short term Funding Solutions for companies, raising anywhere between £20,000 and £25million pounds.

The Card must have a professional look as it is going to be handed out to professionals I.E Solicitors, Accountants, Company directors and Business owners.

See Attached our company Logo

Industry/Entity Type

Business

Contact Information for Business Card

Lewis Thorncroft
Suite 41
R K House
Bramblecote Lane
Elmsworth
HP19 4QX

```html
<!DOCTYPE html>
<html lang="en">
<head>
<meta charset="utf-8">
<title>Harbourline Funding Group – Business Card</title>
<link rel="stylesheet" href="https://fonts.googleapis.com/css2?family=Open+Sans:wght@400;600;700&display=swap">
<style>
  :root {
    --stage: #3b3b3d;
    --brand-blue: #1a64aa;
    --brand-blue-deep: #155793;
    --brand-green: #3a9a3a;
    --card-white: #fbfbfb;
    --card-grey: #e4e4e4;
    --fold: #e9ecef;
    --ink: #2a2a2a;
  }
  * { box-sizing: border-box; margin: 0; padding: 0; }
  html, body {
    width: 1200px; height: 1000px; overflow: hidden;
    background: var(--stage);
    font-family: "Open Sans", sans-serif;
  }
  .stage {
    position: relative; width: 1200px; height: 1000px;
    display: flex; align-items: center; justify-content: center; gap: 60px;
  }
  .card {
    position: relative; width: 520px; height: 300px; overflow: hidden;
    box-shadow: 0 14px 30px rgba(0,0,0,.35);
  }
  .brand {
    display: flex; align-items: center; gap: 12px;
    font-weight: 700; letter-spacing: .04em; text-transform: uppercase;
    white-space: nowrap;
  }
  .brand__dot { border-radius: 50%; flex: none; }

  /* Front */
  .card--front {
    background: radial-gradient(ellipse at 55% 40%, var(--brand-blue) 0%, var(--brand-blue-deep) 100%);
  }
  .card__fold { position: absolute; left: 0; bottom: 0; }
  .card--front .brand {
    position: absolute; top: 128px; left: 0; right: 0; justify-content: center;
    color: #ffffff; font-size: 25px;
  }
  .card--front .brand__dot { width: 20px; height: 20px; background: #ffffff; }

  /* Back */
  .card--back {
    background: radial-gradient(ellipse at 50% 35%, var(--card-white) 0%, var(--card-grey) 100%);
  }
  .card--back .brand {
    position: absolute; top: 54px; left: 0; right: 0; justify-content: center;
    color: var(--brand-blue); font-size: 21px;
  }
  .card--back .brand__dot { width: 16px; height: 16px; background: var(--brand-blue); }
  .divider {
    position: absolute; top: 104px; left: 160px; width: 200px; height: 1px;
    background: linear-gradient(90deg, transparent, var(--brand-green), transparent);
  }
  .holder {
    position: absolute; top: 130px; left: 0; right: 0; text-align: center;
    color: var(--brand-blue); font-size: 19px; font-weight: 400; letter-spacing: .02em;
  }
  .address {
    position: absolute; left: 30px; bottom: 34px;
    display: flex; align-items: center; gap: 10px;
    color: var(--ink); font-size: 13px; white-space: nowrap;
  }
</style>
</head>
<body>
  <main class="stage">
    <section class="card card--front" aria-label="Card front">
      <svg class="card__fold" width="110" height="110" viewBox="0 0 110 110" aria-hidden="true">
        <polygon points="0,30 95,30 0,110" fill="var(--fold)"/>
      </svg>
      <div class="brand"><span class="brand__dot"></span>Harbourline Funding Group</div>
    </section>

    <section class="card card--back" aria-label="Card back">
      <div class="brand"><span class="brand__dot"></span>Harbourline Funding Group</div>
      <div class="divider"></div>
      <p class="holder">Lewis Thorncroft</p>
      <p class="address">
        <svg width="14" height="20" viewBox="0 0 14 20" aria-hidden="true">
          <path d="M7 0C3.1 0 0 3.1 0 7c0 5 7 13 7 13s7-8 7-13c0-3.9-3.1-7-7-7z" fill="var(--brand-green)"/>
          <circle cx="7" cy="7" r="2.6" fill="#ffffff"/>
        </svg>
        Suite 41, R K House, Bramblecote Lane, Elmsworth, HP19 4QX
      </p>
    </section>
  </main>
</body>
</html>
```